Roll label Flyer design

I need a flyer for a roll label printer
Pictures for the project are located here:
https://plimtonstickers.sharefile.com/d-k4wq7812m3a0z551

Text I want is located here:
https://plimtonstickers.com/roll-labels.php

Target Market(s)

Manufactures, wholesalers

Industry/Entity Type

Printing

Requirements
Must have
• Lots of pictures. Our phone number 800-472-8164. Website www.plimtonstickers.com

```html
<!DOCTYPE html>
<html lang="en">
<head>
<meta charset="utf-8">
<title>Plimton Stickers – Roll/Product Labels</title>
<link rel="stylesheet" href="https://fonts.googleapis.com/css2?family=PT+Sans:wght@400;700&family=Oswald:wght@400&display=swap">
<style>
  :root {
    --page: #efefed;
    --ink-dark: #232324;
    --red: #c5111b;
    --red-deep: #8c0a10;
    --white: #ffffff;
    --grey-text: #7a7a7a;
  }
  * { margin: 0; padding: 0; box-sizing: border-box; }
  html, body { width: 796px; height: 1200px; overflow: hidden; background: var(--page); }
  .flyer {
    position: absolute; left: 37px; top: 42px; width: 719px; height: 1110px;
    background: var(--ink-dark); overflow: hidden;
    font-family: "PT Sans", sans-serif; color: var(--white);
    box-shadow: 0 2px 8px rgba(0,0,0,.25);
  }
  .artwork { position: absolute; inset: 0; }
  .brand { position: absolute; left: 160px; top: 34px; display: flex; align-items: center; gap: 18px; }
  .brand-dot { width: 80px; height: 80px; border-radius: 50%; background: var(--red); }
  .brand-name { font-family: "Oswald", sans-serif; font-size: 30px; letter-spacing: 7px; color: #ececec; }
  .title { position: absolute; top: 142px; width: 100%; text-align: center; font-size: 35px; font-weight: 700; }
  .intro {
    position: absolute; left: 24px; top: 256px; width: 336px;
    font-size: 16px; line-height: 18.5px; color: var(--grey-text); text-align: justify;
  }
  .block { position: absolute; left: 26px; }
  .block h2 { font-size: 22px; font-weight: 700; line-height: 25px; margin-bottom: 2px; }
  .block ul { list-style: none; }
  .block li { font-size: 20px; line-height: 25.4px; padding-left: 18px; position: relative; }
  .block li::before { content: "›"; position: absolute; left: 0; top: -1px; font-weight: 700; }
  .features { top: 402px; }
  .markets { top: 587px; }
  .contact { position: absolute; top: 1005px; width: 100%; text-align: center; }
  .phone { font-size: 35px; font-weight: 700; line-height: 40px; }
  .web { font-size: 25px; margin-top: 6px; }
</style>
</head>
<body>
<div class="flyer">
  <svg class="artwork" width="719" height="1110" viewBox="0 0 719 1110">
    <defs>
      <clipPath id="content-area">
        <path d="M0,215 Q360,185 719,285 L719,870 Q380,955 0,915 Z"/>
      </clipPath>
      <radialGradient id="oval-red" cx="0.35" cy="0.45" r="0.7">
        <stop offset="0" stop-color="#d2141e"/>
        <stop offset="0.75" stop-color="#b40f18"/>
        <stop offset="1" stop-color="#7e090e"/>
      </radialGradient>
      <linearGradient id="band-red" x1="0" y1="0" x2="1" y2="0">
        <stop offset="0" stop-color="#a50d15"/>
        <stop offset="0.5" stop-color="#d2141e"/>
        <stop offset="1" stop-color="#9b0c13"/>
      </linearGradient>
      <linearGradient id="photo-shop" x1="0" y1="0" x2="1" y2="1">
        <stop offset="0" stop-color="#c9c6c2"/><stop offset="0.6" stop-color="#6d6660"/><stop offset="1" stop-color="#3a3634"/>
      </linearGradient>
      <linearGradient id="photo-roll" x1="0" y1="0" x2="1" y2="0">
        <stop offset="0" stop-color="#d7d5cf"/><stop offset="0.45" stop-color="#8e8b86"/><stop offset="1" stop-color="#1f1f21"/>
      </linearGradient>
      <linearGradient id="photo-sheet" x1="0" y1="0" x2="1" y2="1">
        <stop offset="0" stop-color="#f0efec"/><stop offset="0.6" stop-color="#9a9896"/><stop offset="1" stop-color="#4a4848"/>
      </linearGradient>
      <linearGradient id="photo-warning" x1="0" y1="0" x2="1" y2="0">
        <stop offset="0" stop-color="#c9421f"/><stop offset="0.5" stop-color="#e9d8cc"/><stop offset="1" stop-color="#d23a25"/>
      </linearGradient>
    </defs>

    <g clip-path="url(#content-area)">
      <rect x="0" y="180" width="719" height="780" fill="#ffffff"/>
      <rect x="385" y="180" width="334" height="310" fill="url(#photo-shop)" role="img" aria-label="Photo: press operator working at a label finishing machine in the print shop"/>
      <rect x="380" y="490" width="339" height="245" fill="url(#photo-roll)" role="img" aria-label="Photo: close-up of a roll of printed black product labels on a press spindle"/>
      <rect x="0" y="735" width="445" height="230" fill="url(#photo-sheet)" role="img" aria-label="Photo: roll of printed safety instruction labels"/>
      <rect x="445" y="735" width="274" height="230" fill="url(#photo-warning)" role="img" aria-label="Photo: rolls of red and white danger warning labels"/>
      <ellipse cx="130" cy="605" rx="290" ry="232" fill="url(#oval-red)"/>
    </g>

    <path d="M0,198 Q360,160 719,250 L719,300 Q360,188 0,216 Z" fill="url(#band-red)"/>
    <path d="M0,912 Q380,955 719,862 L719,905 Q380,1010 0,960 Z" fill="url(#band-red)"/>
  </svg>

  <div class="brand">
    <span class="brand-dot"></span>
    <span class="brand-name">PLIMTON STICKERS</span>
  </div>

  <h1 class="title">Roll/Product Labels</h1>

  <p class="intro">Long or short run. Digital or flexographic. Standard shapes or unique, custom diecuts. Simple spot colors or full color with every embellishment. Let us help you create the perfect label for your<br>application.</p>

  <section class="block features">
    <h2>Features:</h2>
    <ul>
      <li>Foil-stamping</li>
      <li>Embossing</li>
      <li>Spot varnishes</li>
      <li>Instant redeemable coupons</li>
      <li>Expanded content/booklet labels</li>
    </ul>
  </section>

  <section class="block markets">
    <h2>Specialty Markets We<br>Service Include:</h2>
    <ul>
      <li>Health &amp; Beauty</li>
      <li>Food &amp; Beverage</li>
      <li>Wine &amp; Spirits</li>
      <li>Industrial Safety &amp; Warning</li>
      <li>Promotional</li>
      <li>Compliance (i.e. QML, NSB,<br>California Prop 65)</li>
    </ul>
  </section>

  <div class="contact">
    <p class="phone">800-472-8164</p>
    <p class="web">www.plimtonstickers.com</p>
  </div>
</div>
</body>
</html>
```